Business Card Design

It's an investment advisory service for individuals with all there investment needs. Also financial consulting to businesses and governmental agencies on retirement plans etc. It's personalized not commoditized help. Should show strength, knowledge and money orientation.

Industry/Entity Type

Investment

Contact Information for Business Card

B. Vel R. Financial Consulting and Wealth Management, Mirek Dale Hopstein, 5172 Paseo Las Colinas Verde, San Diego, CA 92084-6617, Registered Investment Advisor

Requirements
Nice to have
• Something money oriented

```html
<!DOCTYPE html>
<html lang="en">
<head>
<meta charset="UTF-8">
<title>B. Vel R. Financial Consulting – Business Card</title>
<link rel="stylesheet" href="https://fonts.googleapis.com/css2?family=Open+Sans:wght@700&family=Poppins:wght@600&family=Lato:wght@300;400&display=swap">
<style>
  :root {
    --backdrop: #d6d6d6;
    --card: #282626;
    --name-orange: #f26e21;
    --firm-green: #6cbd45;
    --tagline-white: #ffffff;
    --contact-grey: #cfcfcf;
  }
  * { margin: 0; padding: 0; box-sizing: border-box; }
  html, body {
    width: 1200px;
    height: 900px;
    overflow: hidden;
    background: var(--backdrop);
  }
  .stage {
    width: 1200px;
    height: 900px;
    display: flex;
    align-items: center;
    justify-content: center;
  }
  .business-card {
    position: relative;
    width: 1000px;
    height: 572px;
    background: var(--card);
    box-shadow: 0 10px 30px rgba(0,0,0,0.25);
  }
  .advisor-name {
    position: absolute;
    top: 52px;
    right: 90px;
    font-family: "Open Sans", sans-serif;
    font-weight: 700;
    font-size: 34px;
    color: var(--name-orange);
    letter-spacing: 0.2px;
  }
  .firm-name {
    position: absolute;
    top: 170px;
    left: 130px;
    font-family: "Poppins", sans-serif;
    font-weight: 600;
    font-size: 42px;
    line-height: 1.12;
    color: var(--firm-green);
  }
  .firm-name .second-line {
    display: block;
    padding-left: 62px;
  }
  .tagline {
    position: absolute;
    top: 300px;
    left: 190px;
    font-family: "Lato", sans-serif;
    font-weight: 400;
    font-size: 35px;
    color: var(--tagline-white);
  }
  .contact {
    position: absolute;
    top: 402px;
    left: 500px;
    font-family: "Lato", sans-serif;
    font-weight: 300;
    font-size: 31px;
    line-height: 1.2;
    color: var(--contact-grey);
  }
  .contact-row {
    display: flex;
    align-items: center;
    gap: 14px;
  }
  .contact-row.indented { padding-left: 36px; }
  .contact-row.zip { padding-left: 22px; }
  .contact-icon {
    width: 22px;
    height: 26px;
    fill: var(--contact-grey);
    flex: none;
  }
</style>
</head>
<body>
  <main class="stage">
    <section class="business-card" aria-label="Business card">
      <p class="advisor-name">Mirek Dale Hopstein</p>
      <h1 class="firm-name">
        B. Vel R. Financial Consulting
        <span class="second-line">&amp; Wealth Management</span>
      </h1>
      <p class="tagline">Registered Investment Advisor</p>
      <address class="contact">
        <div class="contact-row">
          <svg class="contact-icon" viewBox="0 0 24 30" aria-hidden="true">
            <path d="M12 0C5.4 0 0 5.2 0 11.6 0 20 12 30 12 30s12-10 12-18.4C24 5.2 18.6 0 12 0zm0 16a4.5 4.5 0 1 1 0-9 4.5 4.5 0 0 1 0 9z"/>
          </svg>
          <span>5172 Paseo Las Colinas Verde,</span>
        </div>
        <div class="contact-row indented"><span>San Diego, CA</span></div>
        <div class="contact-row zip">
          <svg class="contact-icon" viewBox="0 0 24 24" aria-hidden="true">
            <path d="M6.6 10.8a15.2 15.2 0 0 0 6.6 6.6l2.2-2.2c.3-.3.7-.4 1-.2 1.1.4 2.3.6 3.6.6.6 0 1 .4 1 1V20c0 .6-.4 1-1 1C10.6 21 3 13.4 3 4c0-.6.4-1 1-1h3.5c.6 0 1 .4 1 1 0 1.3.2 2.5.6 3.6.1.3 0 .7-.2 1l-2.3 2.2z"/>
          </svg>
          <span>92084-6617,</span>
        </div>
      </address>
    </section>
  </main>
</body>
</html>
```